Business card design needed

My company does everything from wiring up your exisiting entertainment system, to installing a complete new system for you. We can mount your plasma on the wall, install an aerial point for you, setup some surround sound in your outdoor area or install a new cinema room in your house. Any Audio or Visual requirements you may have we can provide these for you. If you want to have a party to remember at your place or just some chilled sounds by the pool, we can give you just the right size system.

Industry/Entity Type

Entertainment

Contact Information for Business Card

The Tune Crew
Colin Pemberton
e| colin@thetunecrew.com.au
w| www.thetunecrew.com.au
m| 0412 576 208

Requirements
Must have
• The logo that i have uploaded is just a starter...something similar to this but not exact or any new suggestions you have would be great too. Colour choice we are pretty easy on we did think Red and Yellow but happy to take advice, something that stands out from the rest i guess.

```html
<!DOCTYPE html>
<html lang="en">
<head>
<meta charset="utf-8">
<title>The Tune Crew – Business Card</title>
<link rel="stylesheet" href="https://fonts.googleapis.com/css2?family=Russo+One&family=Raleway:wght@200;300&display=swap">
<style>
  :root {
    --card-bg: #ffffff;
    --brand-teal: #1d5f7c;
    --name-grey: #6b6b6b;
    --accent-blue: #3c86ab;
    --contact-blue: #5a97b8;
    --mosaic-deep: rgba(58, 146, 190, 0.75);
    --mosaic-light: rgba(150, 205, 235, 0.35);
  }
  html, body {
    margin: 0;
    padding: 0;
    width: 1200px;
    height: 666px;
    overflow: hidden;
    background: var(--card-bg);
  }
  .card {
    position: relative;
    width: 1200px;
    height: 666px;
    background: var(--card-bg);
    overflow: hidden;
  }
  .mosaic-corner {
    position: absolute;
    left: 0;
    top: 0;
    width: 1200px;
    height: 666px;
    background:
      linear-gradient(90deg, var(--mosaic-light) 0%, rgba(255,255,255,0) 22%),
      linear-gradient(135deg, var(--mosaic-deep) 0%, var(--mosaic-light) 22%, rgba(255,255,255,0) 45%);
  }
  .brand-name {
    position: absolute;
    left: 560px;
    width: 584px;
    top: 186px;
    margin: 0;
    text-align: center;
    font-family: "Russo One", sans-serif;
    font-size: 66px;
    font-weight: 400;
    line-height: 1;
    color: var(--brand-teal);
  }
  .person-name {
    position: absolute;
    left: 560px;
    width: 584px;
    top: 292px;
    margin: 0;
    text-align: center;
    font-family: "Raleway", sans-serif;
    font-weight: 200;
    font-size: 50px;
    letter-spacing: 2px;
    line-height: 1;
    text-transform: uppercase;
    color: var(--name-grey);
  }
  .person-role {
    position: absolute;
    left: 560px;
    width: 584px;
    top: 376px;
    margin: 0;
    text-align: center;
    font-family: "Raleway", sans-serif;
    font-weight: 300;
    font-size: 30px;
    letter-spacing: 1px;
    line-height: 1;
    text-transform: uppercase;
    color: var(--accent-blue);
  }
  .divider {
    position: absolute;
    left: 480px;
    top: 472px;
    width: 720px;
    height: 4px;
    background: linear-gradient(90deg, rgba(60,134,171,0) 0%, rgba(60,134,171,0.5) 40%, var(--accent-blue) 100%);
  }
  .contact-list {
    position: absolute;
    left: 604px;
    top: 514px;
    margin: 0;
    padding: 0;
    list-style: none;
    font-family: "Raleway", sans-serif;
    font-weight: 200;
    font-size: 26px;
    letter-spacing: 1px;
    line-height: 43px;
    text-transform: uppercase;
    color: var(--contact-blue);
  }
</style>
</head>
<body>
  <main class="card">
    <div class="mosaic-corner" role="img" aria-label="Corner mosaic of fading blue pixel squares"></div>
    <h1 class="brand-name">The Tune Crew</h1>
    <p class="person-name">Colin Pemberton</p>
    <p class="person-role">Head Boy</p>
    <div class="divider"></div>
    <ul class="contact-list">
      <li>P : +0412 576 208</li>
      <li>E : colin@thetunecrew.com.au</li>
      <li>W : www.thetunecrew.com.au</li>
    </ul>
  </main>
</body>
</html>
```